Tidal Meadow Childcare Recrutment

We need a website for candidates to sign up for jobs in childcare and alternately for nursery companies to be able to sign up to hire either temporary workers or hire permanent staff. The Temps are normally required for 1-14 days and the permanent are normally "Qualified" staff with applicable police checks and first aid, food hygiene, child welfare and safeguarding.

I have the images and copy now, will try to figure out how to upload Added Wednesday, November 18, 2015

Target Market(s)

2 Markets. Employers: 1 - Local child day care nurseries requiring temporary staff to cover sickness, holidays, recruitment shortages. 2 - Same nurseries requiring permanent staff, normally qualified or part qualified.
Candidates: Individuals who are new to childcare or experienced seeking permanent or temporary placements.

Industry/Entity Type

Daycare

Coding

Coded - Design and coding required

Number of Pages Required

4 page

Font styles to use
Sans Serif

Colors
84c9e6

Requirements
Must have
• A split to show Employer vs Job Seeker
• Our Logo..... can send on request (See www.pinebrooknursery.co.uk) for idea it's similar. All part of same company.
• Board to Advertise Current Jobs
• Same day sign up, pay and get temporary staffing
• Ability for Employer or Job Seeker to fill out drop down criteria of basics
• Availability/Requirement Time
• Qualified or Unqualified
• CV email or upload
• Name
• Contact Details
Nice to have
• Testimonials
• Bits or Tasters of CVs to show employers??
Should not have
• Not sure...

```html
<!DOCTYPE html>
<html lang="en">
<head>
<meta charset="utf-8">
<title>Tidal Meadow – Childcare Recruitment</title>
<link href="https://fonts.googleapis.com/css2?family=Raleway:wght@400;500&family=Open+Sans:ital,wght@0,400;0,600;1,400&display=swap" rel="stylesheet">
<style>
:root{
  --sky:#84c9e6;
  --sky-deep:#5fb3da;
  --orange:#ffa200;
  --ink:#333;
  --muted:#777;
  --soft:#999;
  --band:#ececec;
  --navy:#0f3a5a;
  --footer:#000;
}
*{margin:0;padding:0;box-sizing:border-box}
html,body{width:805px;height:1200px;overflow:hidden;background:#fff}
body{position:relative;font-family:"Open Sans",sans-serif;color:var(--ink)}
.abs{position:absolute}
/* header */
.site-header{left:0;top:0;width:805px;height:68px;background:#fff}
.brand{left:121px;top:18px;font-family:"Raleway",sans-serif;font-size:24px;font-weight:500;color:#555;letter-spacing:.3px}
.main-nav a{position:absolute;top:28px;font-family:"Raleway",sans-serif;font-size:10.5px;color:#777;text-decoration:none}
.btn-signup{left:623px;top:24px;width:62px;height:20px;background:var(--sky);color:#fff;font-size:9.5px;font-family:"Raleway",sans-serif;text-align:center;line-height:20px}
/* hero */
.hero{left:0;top:68px;width:805px;height:318px;background:linear-gradient(120deg,#7e6a58 0%,#5a84b0 35%,#8fb6d6 55%,#c9a58f 80%,#8c7a6a 100%)}
.hero-kicker{left:118px;top:178px;font-family:"Raleway",sans-serif;font-size:19px;color:#fff}
.hero-title{left:118px;top:204px;font-family:"Raleway",sans-serif;font-size:32px;color:#fff}
.hero-dots{left:377px;top:362px;display:flex;gap:2px}
.hero-dots span{width:11px;height:11px;border-radius:50%;background:#fff}
.hero-dots span:first-child{background:#111}
/* split */
.split{left:0;top:386px;width:805px;height:136px;background:linear-gradient(#f7f7f7,#ebebeb);border-bottom:1px solid #e0e0e0}
.split-divider{left:0;top:386px}
.audience h2{position:absolute;font-family:"Raleway",sans-serif;font-weight:400;font-size:18px;color:#555}
.audience p{position:absolute;font-size:8.5px;line-height:16px;color:#888;width:200px}
.audience .cta{position:absolute;height:24px;color:#fff;font-size:10px;font-family:"Raleway",sans-serif;text-align:center;line-height:24px}
.icon-circle{position:absolute;width:62px;height:62px;border-radius:50%}
/* featured */
.section-title{font-family:"Raleway",sans-serif;font-size:17.5px;color:#333;font-weight:400}
.seeker{left:121px;width:378px;height:84px}
.seeker-photo{position:absolute;left:0;top:0;width:64px;height:55px;background:linear-gradient(135deg,#8a6f5c,#d2b49d 60%,#e9ddd2)}
.seeker-meta,.seeker-contact{position:absolute;font-size:8px;line-height:16px;color:#666}
.seeker-meta{left:75px;top:-1px}
.seeker-contact{left:208px;top:0;line-height:13px}
.seeker-contact b{font-weight:400;display:block;margin-bottom:2px}
.rule{left:121px;width:378px;height:1px;background:#d8d8d8}
/* sidebar */
.ad-board{left:528px;top:547px;width:151px;height:122px;background:linear-gradient(#a6d8ee,var(--sky-deep));padding:13px 16px;color:#fff}
.ad-board h3{font-family:"Raleway",sans-serif;font-weight:400;font-size:13px;line-height:19px}
.ad-board h3 span{font-size:16.5px}
.ad-board p{font-size:7px;line-height:12px;margin-top:5px;opacity:.95}
.ad-board .btn{display:block;margin-top:9px;width:73px;height:21px;background:var(--navy);font-size:8px;text-align:center;line-height:21px}
.finder{left:528px;top:679px;width:151px;height:153px;border:1px solid #ddd;background:#fff}
.finder h3{height:28px;border-bottom:1px solid #ddd;font-family:"Raleway",sans-serif;font-weight:400;font-size:11.5px;color:#444;padding:8px 0 0 18px;background:#fafafa}
.select{position:absolute;left:18px;width:118px;height:15px;border:1px solid #ccc;font-size:6.5px;color:#777;padding:3px 0 0 7px}
.select svg{position:absolute;right:6px;top:4px}
.btn-find{position:absolute;left:18px;top:117px;width:118px;height:22px;background:var(--sky);color:#fff;font-size:9px;text-align:center;line-height:22px}
/* testimonials */
.testimonials{left:0;top:874px;width:805px;height:244px;background:var(--band)}
.testimonials h2{position:absolute;left:0;width:805px;top:27px;text-align:center;font-family:"Raleway",sans-serif;font-weight:500;font-size:15px;color:#333}
.strip{left:198px;top:74px;width:420px;height:48px;background:linear-gradient(90deg,#444,#aaa 20%,#ddd 35%,#777 55%,#bbb 70%,#333 85%,#ccc)}
.featured-face{left:350px;top:64px;width:64px;height:66px;border:2px solid #fff;background:linear-gradient(#c7a892,#8a4a3e)}
.quote-mark{font-family:Georgia,serif;font-size:34px;color:#444;font-weight:700}
.quote-text{left:200px;top:143px;width:420px;text-align:center;font-style:italic;font-size:8.2px;line-height:14.5px;color:#555}
.author{left:0;width:805px;text-align:center}
/* footer */
.site-footer{left:0;top:1118px;width:805px;height:82px;background:var(--footer);color:#fff}
.footer-links{left:122px;top:19px;font-size:9px}
.copyright{left:122px;top:37px;font-size:7.5px;color:#ccc}
.social{left:620px;top:21px;display:flex;gap:8px}
.social span{width:10px;height:10px;border-radius:50%;background:#fff}
</style>
</head>
<body>

<header class="site-header abs">
  <div class="brand abs">Tidal Meadow</div>
  <nav class="main-nav">
    <a style="left:332px">About</a>
    <a style="left:383px">Find Job</a>
    <a style="left:446px">Post a Job Free!</a>
    <a style="left:542px">Testimonials</a>
  </nav>
  <div class="btn-signup abs">Sign Up</div>
</header>

<section class="hero abs" role="img" aria-label="Photo of three smiling nursery carers in blue uniforms each holding a baby"></section>
<div class="hero-kicker abs">Praesent sit amet dictum dolor</div>
<div class="hero-title abs">Dictum porttitor enim</div>
<div class="hero-dots abs"><span></span><span></span><span></span><span></span></div>

<section class="split abs"></section>
<svg class="split-divider abs" width="805" height="136" viewBox="0 0 805 136">
  <polygon points="413,0 805,0 805,136 377,136" fill="#f1f1f1"/>
  <line x1="413" y1="0" x2="377" y2="136" stroke="#e3e3e3"/>
</svg>

<div class="audience">
  <div class="icon-circle" style="left:128px;top:419px;background:var(--orange)">
    <svg width="62" height="62" viewBox="0 0 62 62"><circle cx="34" cy="27" r="12" fill="none" stroke="#fff" stroke-width="3"/><circle cx="34" cy="23" r="4" fill="#fff"/><path d="M27 33a7 6 0 0 1 14 0z" fill="#fff"/><line x1="25" y1="36" x2="16" y2="45" stroke="#fff" stroke-width="4" stroke-linecap="round"/></svg>
  </div>
  <h2 style="left:202px;top:416px">For Job Seekers</h2>
  <p style="left:202px;top:439px">Curabitur pede aecenas aliquet velit vel turpis Mauris neque metus malesuada nec</p>
  <div class="cta" style="left:202px;top:476px;width:87px;background:var(--orange)">Job Seeker</div>

  <div class="icon-circle" style="left:414px;top:416px;background:var(--sky)">
    <svg width="62" height="62" viewBox="0 0 62 62"><rect x="16" y="22" width="30" height="22" fill="none" stroke="#fff" stroke-width="2"/><path d="M26 22v-4h10v4M16 30h30M31 28v4" fill="none" stroke="#fff" stroke-width="2"/></svg>
  </div>
  <h2 style="left:487px;top:413px">For Employers</h2>
  <p style="left:487px;top:436px">Curabitur pede aecenas aliquet velit vel turpis Mauris neque metus malesuada nec</p>
  <div class="cta" style="left:488px;top:472px;width:87px;background:var(--sky)">Employers</div>
</div>

<h2 class="section-title abs" style="left:122px;top:551px">Featured Job Seekers</h2>

<article class="seeker abs" style="top:592px">
  <div class="seeker-photo" role="img" aria-label="Portrait photo of a job seeker"></div>
  <div class="seeker-meta">Name:&nbsp; Anna Rell Kemp<br>Qualification:&nbsp; Graduate<br><span style="line-height:22px">View CV</span></div>
  <div class="seeker-contact"><b>Contact Information</b>412 Harbor Lane Suite B20<br>Millbrook, PA 19100<br>Phone: (555) 014-2200</div>
</article>
<div class="rule abs" style="top:662px"></div>
<article class="seeker abs" style="top:676px">
  <div class="seeker-photo" role="img" aria-label="Portrait photo of a job seeker"></div>
  <div class="seeker-meta">Name:&nbsp; Anna Rell Kemp<br>Qualification:&nbsp; Graduate<br><span style="line-height:22px">View CV</span></div>
  <div class="seeker-contact"><b>Contact Information</b>412 Harbor Lane Suite B20<br>Millbrook, PA 19100<br>Phone: (555) 014-2200</div>
</article>
<div class="rule abs" style="top:746px"></div>
<article class="seeker abs" style="top:760px">
  <div class="seeker-photo" role="img" aria-label="Portrait photo of a job seeker"></div>
  <div class="seeker-meta">Name:&nbsp; Anna Rell Kemp<br>Qualification:&nbsp; Graduate<br><span style="line-height:22px">View CV</span></div>
  <div class="seeker-contact"><b>Contact Information</b>412 Harbor Lane Suite B20<br>Millbrook, PA 19100<br>Phone: (555) 014-2200</div>
</article>

<aside class="ad-board abs">
  <h3>Advertise<br><span>Current Jobs</span></h3>
  <p>Curabitur pedeMaecenas aliquet velit vel turpis Mauris nequ</p>
  <span class="btn">Send me jobs</span>
</aside>

<aside class="finder abs">
  <h3>Find Jobs/Employers</h3>
  <div class="select" style="top:37px">Criteria of basics<svg width="7" height="5"><path d="M0 0l3.5 4L7 0" fill="none" stroke="#888"/></svg></div>
  <div class="select" style="top:57px">Locations<svg width="7" height="5"><path d="M0 0l3.5 4L7 0" fill="none" stroke="#888"/></svg></div>
  <div class="select" style="top:78px">Qualification<svg width="7" height="5"><path d="M0 0l3.5 4L7 0" fill="none" stroke="#888"/></svg></div>
  <div class="select" style="top:97px">Timing Prefer<svg width="7" height="5"><path d="M0 0l3.5 4L7 0" fill="none" stroke="#888"/></svg></div>
  <div class="btn-find">FIND NOW</div>
</aside>

<section class="testimonials abs">
  <h2>TESTIMONIALS</h2>
  <div class="quote-mark abs" style="left:170px;top:50px">&ldquo;</div>
  <div class="strip abs" role="img" aria-label="Row of black and white portrait photos of past clients"></div>
  <div class="featured-face abs" role="img" aria-label="Colour portrait photo of the quoted client"></div>
  <div class="quote-mark abs" style="left:620px;top:114px">&rdquo;</div>
  <p class="quote-text abs">At nisi erat fermentum vel congue id euismod in elit Fusce ultricies orci ac feugiat suscipit leo massa sodales velit et scelerisque mi tortor at ipsum cligula augue bibendum accumsan vestibulum ut commodo a mi Morbi ornare gravida elit Integer congue augue et</p>
  <div class="author abs" style="top:188px;font-size:10px;color:#333">By Hazel Dunmore</div>
  <div class="author abs" style="top:204px;font-size:7px;color:#555">City Location</div>
</section>

<footer class="site-footer abs">
  <div class="footer-links abs">Home&nbsp; | &nbsp;Products&nbsp; | &nbsp;Partners&nbsp; | &nbsp;Support&nbsp; | &nbsp;About&nbsp; | &nbsp;News&nbsp; | &nbsp;Careers&nbsp; | &nbsp;Contact</div>
  <div class="copyright abs">© 2015 Company Name&nbsp; All right reserved&nbsp; Term of Use</div>
  <div class="social abs"><span></span><span></span><span></span><span></span></div>
</footer>

</body>
</html>
```